Ordnerdesign für Experte für Versicherungs - und Haftungsfragen im Etiketten - und Verpackungsdruck
Ordnerdesign für Experte für Versicherungs - und Haftungsfragen im Etiketten - und Verpackungsdr..
Zielgruppe
Ich bin Henrik Wallmoser Experte für Versicherungs - und Haftungsfragen im Etiketten - und Verpackungsdruck (meine CI Farben sind orange /schwarz ) Meine Company und das Produkt ist die tarvolink und der tarvolnk Schutzbrief für Druckerereien (schwarz/gelb)
Aufgabenstellung
Gesucht wird für mein/unser Projekt : Ordnerdesign PLUS Register eines Notfallhandbuchs für Unternehmer . Es gibt zwei Produktlinien - zu beiden ist jeweils der Farbfächer /Broschüre beigefügt : Entweder der Notfallordner soll unter ' Henrik Wallmoser Experte für Haftungsfragen .. ( Orange Schwarz oder die Farben meiner Company ( tarvolink Schwarz - gelb ) siehe Broschüre angelegt werden. freie Hand , was also besser passt .

```html
<!DOCTYPE html>
<html lang="de">
<head>
<meta charset="utf-8">
<title>Henrik Wallmoser – Notfallordner</title>
<link rel="stylesheet" href="https://fonts.googleapis.com/css2?family=Montserrat:wght@500&display=swap">
<style>
  :root {
    --backdrop: #dedede;
    --cover-black: #3a3a3a;
    --cover-black-deep: #2e2e2e;
    --brand-orange: #d4380f;
    --brand-orange-dark: #a8260c;
    --mark-orange: #f2542d;
  }
  html, body {
    margin: 0;
    padding: 0;
    width: 1200px;
    height: 933px;
    overflow: hidden;
    background: var(--backdrop);
  }
  .canvas {
    position: relative;
    width: 1200px;
    height: 933px;
    display: flex;
    align-items: center;
    justify-content: center;
    gap: 48px;
  }
  .folder-cover {
    position: relative;
    width: 460px;
    height: 650px;
    background: linear-gradient(160deg, var(--cover-black) 0%, var(--cover-black-deep) 100%);
    box-shadow: 0 20px 40px rgba(0,0,0,0.18);
  }
  .cover-name {
    position: absolute;
    top: 150px;
    left: 0;
    right: 0;
    text-align: center;
    font-family: "Montserrat", sans-serif;
    font-weight: 500;
    font-size: 30px;
    letter-spacing: 0.02em;
    color: var(--mark-orange);
    margin: 0;
  }
  .folder-inside {
    position: relative;
    width: 460px;
    height: 650px;
    background: linear-gradient(200deg, var(--brand-orange-dark) 0%, var(--brand-orange) 100%);
    box-shadow: 0 20px 40px rgba(0,0,0,0.18);
  }
  .folder-inside svg {
    position: absolute;
    inset: 0;
  }
</style>
</head>
<body>
  <main class="canvas">
    <section class="folder-cover" aria-label="Ordner Vorderseite">
      <h1 class="cover-name">Henrik Wallmoser</h1>
    </section>
    <section class="folder-inside" aria-label="Ordner Innenseite mit Einstecktasche">
      <svg width="460" height="650" viewBox="0 0 460 650" aria-hidden="true">
        <path class="pocket" d="M0 330 L150 330 A250 250 0 0 1 400 580 L400 650 L0 650 Z"
              fill="var(--brand-orange)"/>
        <path class="pocket-edge" d="M150 330 A250 250 0 0 1 400 580 L400 650"
              fill="none" stroke="rgba(0,0,0,0.22)" stroke-width="2"/>
      </svg>
    </section>
  </main>
</body>
</html>
```